Landing Page für Anbieter von Finanzierungslösungen
Zielgruppe
Finanzierungslösungen für Gewerbe und Firmen. Fokus liegt auf der Finanzierung von Rechenzentren und deren Einrichtung.
Aufgabenstellung
Wir haben bereits Visitenkarten und Briefbögen designen lassen. Bitte daran anlehnen.

```html
<!DOCTYPE html>
<html lang="de">
<head>
<meta charset="utf-8">
<title>Velacap – Finanzierung für Gewerbe und Rechenzentren</title>
<link href="https://fonts.googleapis.com/css2?family=Inter:wght@400;500;600;700&display=swap" rel="stylesheet">
<style>
:root{
  --navy:#070b1e;
  --navy-2:#0d1433;
  --navy-card:#121a38;
  --line-dark:#222b4d;
  --green:#9ad600;
  --green-dark:#7fb300;
  --blue:#2f6fe4;
  --ink:#111827;
  --muted:#6b7280;
  --soft:#f5f7fa;
  --border:#e5e7eb;
  --white:#ffffff;
}
*{box-sizing:border-box;margin:0;padding:0}
html,body{width:1200px;height:4749px;overflow:hidden}
body{font-family:"Inter",sans-serif;color:var(--ink);background:var(--white);font-size:14px;line-height:1.5}
.wrap{width:1026px;margin:0 auto;position:relative;height:100%}
svg.ic{width:20px;height:20px;fill:none;stroke:currentColor;stroke-width:1.7;stroke-linecap:round;stroke-linejoin:round}
.btn{display:inline-flex;align-items:center;gap:8px;border-radius:6px;font-weight:600;font-size:14px;white-space:nowrap}
.btn svg{width:14px;height:14px}
.btn-green{background:var(--green);color:var(--navy)}
.btn-ghost{border:1px solid #3a4364;color:var(--white)}

/* nav */
.nav{height:66px;background:var(--navy);border-bottom:1px solid var(--line-dark)}
.nav .wrap{display:flex;align-items:center}
.brand{display:flex;align-items:center;gap:8px;font-weight:700;font-size:24px;color:var(--white)}
.brand i{width:10px;height:10px;background:var(--green);display:block;border-radius:2px}
.nav-links{display:flex;gap:24px;margin-left:26px;font-size:13px;color:#d7dbe8}
.nav-actions{margin-left:auto;display:flex;gap:14px}
.nav-actions .btn{height:38px;padding:0 16px;font-size:13px}

/* hero */
.hero{height:701px;background:radial-gradient(ellipse at 25% 20%,#1a2a66 0%,var(--navy) 60%)}
.badge{position:absolute;top:104px;left:0;font-size:11px;color:#a9c3ff;border:1px solid #2b3f7a;border-radius:20px;padding:3px 10px;background:#101a40}
.hero h1{position:absolute;top:145px;left:0;width:500px;font-size:49px;line-height:50px;font-weight:700;color:var(--white);letter-spacing:-1px}
.hero h1 em{font-style:normal;color:var(--green)}
.hero .lead{position:absolute;top:366px;left:0;width:470px;font-size:16px;line-height:27px;color:#c7cde0}
.hero .cta{position:absolute;top:455px;left:0;display:flex;gap:14px}
.hero .cta .btn{height:52px;padding:0 26px;font-size:15px}
.checks{position:absolute;top:538px;left:0;font-size:11.5px;color:#aab2c8;display:flex;flex-wrap:wrap;width:340px;gap:10px 16px}
.checks span{display:flex;align-items:center;gap:6px}
.checks svg{width:13px;height:13px;color:var(--green)}
.panel{position:absolute;top:94px;left:540px;width:486px;height:498px;border:1px solid var(--line-dark);border-radius:14px;background:linear-gradient(160deg,#111a3d,#0a1029)}
.mini{position:absolute;display:flex;align-items:center;gap:12px;border:1px solid #2e3860;background:#141d42;border-radius:8px;padding:0 14px;width:214px;height:62px}
.mini .sq{width:30px;height:30px;border-radius:6px;display:grid;place-items:center;flex:none}
.mini .sq svg{width:16px;height:16px}
.mini b{display:block;font-size:12px;color:var(--white);font-weight:600}
.mini small{display:block;font-size:9.5px;color:#8d96b3}
.chart{position:absolute;left:28px;top:276px;width:266px;height:180px;border:1px solid #2a345a;border-radius:10px;background:#0f1735;padding:20px}
.chart small{font-size:11px;color:#8d96b3}
.chart strong{display:block;color:var(--white);font-size:24px;font-weight:600;margin-top:4px}
.bars{position:absolute;left:20px;bottom:40px;display:flex;align-items:flex-end;gap:6px}
.bars i{display:block;width:36px}
.chart .up{position:absolute;left:20px;bottom:16px;font-size:9.5px;color:var(--green)}

/* features strip */
.strip{height:210px;border-bottom:1px solid var(--border)}
.strip .wrap{display:grid;grid-template-columns:repeat(4,1fr)}
.feat{text-align:center;padding:34px 18px 0;border-right:1px solid var(--border);height:158px;margin-top:26px;padding-top:8px}
.feat:last-child{border-right:0}
.ibox{width:38px;height:38px;border-radius:50%;background:#eef1f7;display:grid;place-items:center;margin:0 auto 14px;color:#4b5b86}
.ibox svg{width:17px;height:17px}
.feat h3{font-size:16px;font-weight:600;line-height:23px}
.feat p{font-size:12.5px;color:var(--muted);margin-top:6px;line-height:19px}

/* solutions */
.solutions{height:608px;background:var(--soft)}
.sec-title{text-align:center;font-size:29px;font-weight:600;padding-top:80px;letter-spacing:-.3px}
.sec-sub{text-align:center;color:var(--muted);font-size:15px;margin-top:6px}
.cards{display:grid;grid-template-columns:repeat(5,1fr);gap:21px;margin-top:60px}
.card{background:var(--white);border:1px solid var(--border);border-radius:10px;height:320px;padding:30px 26px;position:relative}
.card .ibox{margin:0 0 30px;border-radius:8px;background:#edf2fd;color:var(--blue);width:34px;height:34px}
.card h3{font-size:16px;font-weight:600;line-height:23px;min-height:46px;display:flex;align-items:flex-end}
.card p{font-size:12.5px;color:var(--muted);line-height:20px;margin-top:12px}
.more{position:absolute;left:26px;bottom:30px;color:var(--blue);font-size:13.5px;font-weight:500;display:flex;align-items:center;gap:6px}
.more svg{width:12px;height:12px}

/* focus */
.focus{height:826px;background:linear-gradient(180deg,#070b1e,#080e28 60%,#070b1e)}
.focus-visual{position:absolute;left:0;top:162px;width:484px;height:500px;border-radius:12px;background:linear-gradient(160deg,#24356f,#162352 55%,#0f1a3d);border:1px solid #2a3766}
.eyebrow{font-size:11px;font-weight:600;letter-spacing:.6px;color:var(--green);text-transform:uppercase}
.focus .eyebrow{position:absolute;left:540px;top:82px}
.focus h2{position:absolute;left:540px;top:105px;width:480px;font-size:42px;line-height:42px;font-weight:600;color:var(--white);letter-spacing:-.6px}
.focus .lead{position:absolute;left:540px;top:210px;width:480px;font-size:15.5px;line-height:27px;color:#c3c9dc}
.fgrid{position:absolute;left:540px;top:352px;width:486px;display:grid;grid-template-columns:1fr 1fr;gap:20px 18px}
.fcard{height:142px;border:1px solid #2a3358;border-radius:8px;background:#10173a;padding:18px}
.fcard .sq{width:30px;height:30px;border-radius:6px;background:#1c3a1a;color:var(--green);display:grid;place-items:center;margin-bottom:26px}
.fcard .sq svg{width:15px;height:15px}
.fcard b{display:block;color:var(--white);font-size:14px;font-weight:600}
.fcard small{display:block;color:#8d96b3;font-size:11px;line-height:16px;margin-top:6px}
.focus .proj{position:absolute;left:540px;top:697px;height:50px;padding:0 26px}

/* steps */
.steps{height:403px;border-bottom:1px solid var(--border)}
.steps .sec-title{padding-top:82px}
.srow{display:grid;grid-template-columns:repeat(4,1fr);margin-top:60px;position:relative}
.srow:before{content:"";position:absolute;top:22px;left:13%;right:13%;height:1px;background:var(--border)}
.step{text-align:center;position:relative;padding:0 20px}
.step .c{width:44px;height:44px;border-radius:50%;background:var(--white);border:1px solid var(--border);display:grid;place-items:center;margin:0 auto;color:#4b5b86;position:relative}
.step .c svg{width:18px;height:18px}
.step .n{position:absolute;top:-8px;right:-8px;width:19px;height:19px;border-radius:50%;background:var(--blue);color:var(--white);font-size:10px;font-weight:600;display:grid;place-items:center}
.step h3{font-size:16.5px;font-weight:600;margin-top:14px}
.step p{font-size:12.5px;color:var(--muted);line-height:19px;margin-top:6px}

/* form */
.inquiry{height:721px;background:var(--soft)}
.inquiry h2{position:absolute;top:84px;font-size:25px;font-weight:600}
.inquiry .sub{position:absolute;top:124px;color:var(--muted);font-size:15px}
.form{position:absolute;top:172px;left:0;width:593px;height:453px;background:var(--white);border:1px solid var(--border);border-radius:10px;padding:26px}
.field{height:40px;border:1px solid var(--border);border-radius:5px;background:#fafbfc;font-size:12px;color:#9aa1ae;padding:0 14px;display:flex;align-items:center}
.frow{display:grid;grid-template-columns:1fr 1fr;gap:18px;margin-bottom:18px}
.field.full{margin-bottom:18px;justify-content:space-between;color:#6b7280}
.field.full svg{width:12px;height:12px}
.field.area{height:100px;align-items:flex-start;padding-top:12px}
.consent{display:flex;align-items:center;gap:10px;font-size:11px;color:var(--muted);margin-top:10px}
.consent i{width:14px;height:14px;border:1px solid #c9ced8;border-radius:3px;display:block}
.consent a{color:var(--blue)}
.form .submit{margin-top:30px;width:100%;height:50px;justify-content:center;font-size:14.5px}
.side{position:absolute;left:648px;width:378px;background:var(--white);border:1px solid var(--border);border-radius:10px;padding:28px 28px 28px 80px}
.side .ico{position:absolute;left:28px;top:30px;width:34px;height:34px;border-radius:50%;background:#edf2fd;color:var(--blue);display:grid;place-items:center}
.side .ico svg{width:17px;height:17px}
.side h3{font-size:15.5px;font-weight:600;line-height:23px}
.side ul{list-style:none;margin-top:14px}
.side li{display:flex;align-items:center;gap:8px;font-size:13px;color:var(--muted);margin-bottom:10px}
.side li svg{width:14px;height:14px;color:var(--green-dark)}
.side p{font-size:13px;color:var(--muted);line-height:20px;margin-top:4px}
.side .link{display:flex;align-items:center;gap:6px;color:var(--blue);font-size:13px;font-weight:500;margin-top:10px}
.side .link svg{width:12px;height:12px}

/* about */
.about{height:409px}
.about .eyebrow{position:absolute;top:85px;color:#4b5563;font-size:9.5px}
.about h2{position:absolute;top:106px;font-size:30px;font-weight:600;letter-spacing:-.4px}
.about .txt{position:absolute;top:170px;width:470px;color:#4b5563;font-size:15.5px;line-height:23px}
.about .txt p+p{margin-top:18px}
.vals{position:absolute;left:540px;top:107px;width:486px;display:grid;grid-template-columns:1fr 1fr;gap:34px 40px}
.val svg{width:26px;height:26px;color:var(--blue);stroke-width:1.5}
.val b{display:block;font-size:14px;font-weight:600;margin-top:12px}
.val p{font-size:12.5px;color:var(--muted);line-height:19px;margin-top:6px}
.val.wide{grid-column:1/3}

/* cta */
.ctawrap{height:452px}
.ctabox{position:absolute;top:52px;left:0;width:1026px;height:319px;border-radius:16px;background:radial-gradient(ellipse at 50% 0%,#1a2550,var(--navy) 70%);text-align:center;box-shadow:0 14px 30px rgba(7,11,30,.18)}
.ctabox h2{color:var(--white);font-size:30px;font-weight:600;margin-top:76px}
.ctabox p{color:#c3c9dc;font-size:15.5px;line-height:23px;width:560px;margin:20px auto 0}
.ctabox .acts{display:flex;justify-content:center;gap:14px;margin-top:36px}
.ctabox .btn{height:50px;padding:0 26px}

/* footer */
.footer{height:353px;border-top:1px solid var(--border)}
.fcol{position:absolute;top:55px}
.flogo{width:140px;height:66px;background:var(--navy);border-radius:4px;display:flex;align-items:center;justify-content:center;gap:8px;color:var(--white);font-weight:700;font-size:22px}
.flogo i{width:9px;height:9px;background:var(--green);display:block;border-radius:2px}
.addr{margin-top:22px;font-size:13px;line-height:24px;color:#4b5563}
.addr b{color:var(--ink);font-weight:600}
.fcol h4{font-size:12px;font-weight:600;letter-spacing:1px;text-transform:uppercase;margin-top:0}
.fcol ul{list-style:none;margin-top:12px}
.fcol li{font-size:13px;color:#4b5563;line-height:30px;display:flex;align-items:center;gap:10px}
.fcol li svg{width:15px;height:15px;color:#6b7280}
.copy{position:absolute;left:0;right:0;bottom:0;height:46px;border-top:1px solid var(--border);text-align:center;font-size:11px;color:var(--muted);line-height:46px}
</style>
</head>
<body>

<header class="nav">
  <div class="wrap">
    <div class="brand"><i></i>velacap</div>
    <nav class="nav-links">
      <span>Finanzierung ▾</span><span>Baufinanzierung</span><span>Versicherungen</span><span>Kapitalanlage</span><span>Über uns</span>
    </nav>
    <div class="nav-actions">
      <span class="btn btn-ghost">Termin vereinbaren <svg class="ic" viewBox="0 0 24 24"><rect x="3" y="5" width="18" height="16" rx="2"/><path d="M3 10h18M8 3v4M16 3v4"/></svg></span>
      <span class="btn btn-green">Anfrage stellen</span>
    </div>
  </div>
</header>

<section class="hero">
  <div class="wrap">
    <span class="badge">Finanzierungslösungen für Unternehmen</span>
    <h1>Kapital für Wachstum, Infrastruktur und <em>Rechenzentren.</em></h1>
    <p class="lead">velacap unterstützt Gewerbe und Firmen mit klaren Finanzierungslösungen – einfach, schnell und persönlich.</p>
    <div class="cta">
      <span class="btn btn-green">Anfrage stellen <svg class="ic" viewBox="0 0 24 24"><path d="M5 12h14M13 6l6 6-6 6"/></svg></span>
      <span class="btn btn-ghost">Termin vereinbaren <svg class="ic" viewBox="0 0 24 24"><rect x="3" y="5" width="18" height="16" rx="2"/><path d="M3 10h18M8 3v4M16 3v4"/></svg></span>
    </div>
    <div class="checks">
      <span><svg class="ic" viewBox="0 0 24 24"><circle cx="12" cy="12" r="9"/><path d="M8 12l3 3 5-6"/></svg>Persönliche Beratung</span>
      <span><svg class="ic" viewBox="0 0 24 24"><circle cx="12" cy="12" r="9"/><path d="M8 12l3 3 5-6"/></svg>Schnelle Rückmeldung</span>
      <span><svg class="ic" viewBox="0 0 24 24"><circle cx="12" cy="12" r="9"/><path d="M8 12l3 3 5-6"/></svg>Lösungen für Gewerbe &amp; Unternehmen</span>
    </div>

    <div class="panel">
      <div class="mini" style="left:232px;top:26px">
        <span class="sq" style="background:#233166;color:#8fb0ff"><svg class="ic" viewBox="0 0 24 24"><rect x="4" y="4" width="16" height="7" rx="1.5"/><rect x="4" y="13" width="16" height="7" rx="1.5"/></svg></span>
        <span><b>Rechenzentrum</b><small>Finanzierung von RZ</small></span>
      </div>
      <div class="mini" style="left:206px;top:102px">
        <span class="sq" style="background:#1d3b2a;color:var(--green)"><svg class="ic" viewBox="0 0 24 24"><rect x="6" y="6" width="12" height="12" rx="2"/><path d="M9 3v3M15 3v3M9 18v3M15 18v3M3 9h3M3 15h3M18 9h3M18 15h3"/></svg></span>
        <span><b>Einrichtung &amp; Infrastruktur</b><small>Technik, Energie &amp; Ausstattung</small></span>
      </div>
      <div class="mini" style="left:246px;top:178px">
        <span class="sq" style="background:#33245e;color:#b79cff"><svg class="ic" viewBox="0 0 24 24"><rect x="4" y="7" width="16" height="13" rx="2"/><path d="M9 7V4h6v3"/></svg></span>
        <span><b>Gewerbefinanzierung</b><small>Kapital für Ihr Unternehmen</small></span>
      </div>
      <div class="chart">
        <small>Finanzierungsvolumen</small>
        <strong>12,8 Mio. €</strong>
        <div class="bars">
          <i style="height:16px;background:#3553b3"></i>
          <i style="height:26px;background:#3a5bc4"></i>
          <i style="height:20px;background:#3a5bc4"></i>
          <i style="height:40px;background:#5f8a1e"></i>
          <i style="height:54px;background:#7eb01a"></i>
        </div>
        <span class="up">↗ +15% zum Vorquartal</span>
      </div>
    </div>
  </div>
</section>

<section class="strip">
  <div class="wrap">
    <div class="feat"><div class="ibox"><svg class="ic" viewBox="0 0 24 24"><rect x="5" y="3" width="14" height="18" rx="1.5"/><path d="M9 7h2M13 7h2M9 11h2M13 11h2M10 21v-4h4v4"/></svg></div><h3>Finanzierung für Gewerbe<br>&amp; Firmen</h3><p>Individuelle Lösungen für<br>Unternehmen jeder Größe.</p></div>
    <div class="feat"><div class="ibox"><svg class="ic" viewBox="0 0 24 24"><rect x="4" y="4" width="16" height="7" rx="1.5"/><rect x="4" y="13" width="16" height="7" rx="1.5"/></svg></div><h3>Fokus auf Rechenzentren<br>&amp; Ausstattung</h3><p>Spezialisiert auf digitale<br>Infrastruktur und Technik.</p></div>
    <div class="feat"><div class="ibox"><svg class="ic" viewBox="0 0 24 24"><circle cx="9" cy="8" r="3.5"/><path d="M3 20c0-3.3 2.7-6 6-6s6 2.7 6 6M16 4.5a3.5 3.5 0 010 7M21 20c0-2.6-1.6-4.8-4-5.6"/></svg></div><h3>Persönliche<br>Ansprechpartner</h3><p>Direkte Kommunikation und<br>echte Partnerschaft.</p></div>
    <div class="feat"><div class="ibox"><svg class="ic" viewBox="0 0 24 24"><path d="M12 3l8 3v6c0 4.5-3.4 8-8 9-4.6-1-8-4.5-8-9V6z"/><path d="M9 12l2 2 4-4"/></svg></div><h3>Flexible Lösungen statt<br>Standardprodukt</h3><p>Maßgeschneidert statt von der<br>Stange.</p></div>
  </div>
</section>

<section class="solutions">
  <div class="wrap">
    <h2 class="sec-title">Unsere Lösungen für Ihren Erfolg</h2>
    <p class="sec-sub">Klar. Einfach. Passend für Ihr Unternehmen.</p>
    <div class="cards">
      <div class="card"><div class="ibox"><svg class="ic" viewBox="0 0 24 24"><ellipse cx="12" cy="6" rx="7" ry="3"/><path d="M5 6v12c0 1.7 3.1 3 7 3s7-1.3 7-3V6M5 12c0 1.7 3.1 3 7 3s7-1.3 7-3"/></svg></div><h3>Rechenzentrums-<br>finanzierung</h3><p>Finanzierung von Rechenzentren, Technik, Energieversorgung und Infrastruktur.</p><span class="more">Mehr erfahren <svg class="ic" viewBox="0 0 24 24"><path d="M5 12h14M13 6l6 6-6 6"/></svg></span></div>
      <div class="card"><div class="ibox"><svg class="ic" viewBox="0 0 24 24"><rect x="4" y="7" width="16" height="13" rx="2"/><path d="M9 7V4h6v3M9 7v13M15 7v13"/></svg></div><h3>Gewerbe-<br>finanzierung</h3><p>Kapital für Investitionen, Wachstum, Betriebsmittel und Unternehmensziele.</p><span class="more">Mehr erfahren <svg class="ic" viewBox="0 0 24 24"><path d="M5 12h14M13 6l6 6-6 6"/></svg></span></div>
      <div class="card"><div class="ibox"><svg class="ic" viewBox="0 0 24 24"><path d="M4 11l8-7 8 7v9H4z"/><path d="M10 20v-5h4v5"/></svg></div><h3>Baufinanzierung</h3><p>Finanzierung von Gewerbeimmobilien, Neubau, Ausbau und Modernisierung.</p><span class="more">Mehr erfahren <svg class="ic" viewBox="0 0 24 24"><path d="M5 12h14M13 6l6 6-6 6"/></svg></span></div>
      <div class="card"><div class="ibox"><svg class="ic" viewBox="0 0 24 24"><path d="M12 3l8 3v6c0 4.5-3.4 8-8 9-4.6-1-8-4.5-8-9V6z"/></svg></div><h3>Versicherungen</h3><p>Individuelle Absicherung für Unternehmen, Mitarbeiter und Geschäftsrisiken.</p><span class="more">Mehr erfahren <svg class="ic" viewBox="0 0 24 24"><path d="M5 12h14M13 6l6 6-6 6"/></svg></span></div>
      <div class="card"><div class="ibox"><svg class="ic" viewBox="0 0 24 24"><path d="M4 4v16h16"/><path d="M7 15l4-4 3 3 5-6"/></svg></div><h3>Kapitalanlage</h3><p>Strategische Kapitalanlagen für Unternehmen und Privatkunden.</p><span class="more">Mehr erfahren <svg class="ic" viewBox="0 0 24 24"><path d="M5 12h14M13 6l6 6-6 6"/></svg></span></div>
    </div>
  </div>
</section>

<section class="focus">
  <div class="wrap">
    <div class="focus-visual" role="img" aria-label="Illustration eines Serverracks als Sinnbild für Rechenzentren"></div>
    <span class="eyebrow">Unser Schwerpunkt</span>
    <h2>Finanzierung für digitale Infrastruktur.</h2>
    <p class="lead">Rechenzentren erfordern hohe Investitionen in Gebäude, Technik, Energieversorgung und Ausstattung. velacap begleitet Unternehmen mit passenden Finanzierungslösungen.</p>
    <div class="fgrid">
      <div class="fcard"><span class="sq"><svg class="ic" viewBox="0 0 24 24"><rect x="6" y="6" width="12" height="12" rx="2"/><path d="M9 3v3M15 3v3M9 18v3M15 18v3M3 9h3M3 15h3M18 9h3M18 15h3"/></svg></span><b>Infrastruktur finanzieren</b><small>Gebäude, Energie, Kühlung und Netzwerke.</small></div>
      <div class="fcard"><span class="sq"><svg class="ic" viewBox="0 0 24 24"><rect x="4" y="6" width="16" height="12" rx="2"/><path d="M4 12h16M8 15h.01"/></svg></span><b>Ausstattung realisieren</b><small>Server, Storage, Racks und IT-Hardware.</small></div>
      <div class="fcard"><span class="sq"><svg class="ic" viewBox="0 0 24 24"><path d="M4 17l6-6 4 4 6-7"/><path d="M15 8h5v5"/></svg></span><b>Wachstum planbar machen</b><small>Liquidität sichern und in die Zukunft investieren.</small></div>
    </div>
    <span class="btn btn-green proj">Projekt anfragen <svg class="ic" viewBox="0 0 24 24"><path d="M5 12h14M13 6l6 6-6 6"/></svg></span>
  </div>
</section>

<section class="steps">
  <div class="wrap">
    <h2 class="sec-title">So einfach finanzieren wir gemeinsam</h2>
    <div class="srow">
      <div class="step"><div class="c"><svg class="ic" viewBox="0 0 24 24"><path d="M6 3h9l4 4v14H6z"/><path d="M9 12h6M9 16h6"/></svg><span class="n">1</span></div><h3>Anfrage stellen</h3><p>Nennen Sie uns Ihr Vorhaben in<br>wenigen Minuten.</p></div>
      <div class="step"><div class="c"><svg class="ic" viewBox="0 0 24 24"><circle cx="9" cy="8" r="3.5"/><path d="M3 20c0-3.3 2.7-6 6-6s6 2.7 6 6M16 4.5a3.5 3.5 0 010 7M21 20c0-2.6-1.6-4.8-4-5.6"/></svg><span class="n">2</span></div><h3>Bedarf klären</h3><p>Wir hören zu und verstehen Ihre<br>Anforderungen.</p></div>
      <div class="step"><div class="c"><svg class="ic" viewBox="0 0 24 24"><rect x="6" y="4" width="12" height="17" rx="1.5"/><path d="M9 4V3h6v1M9 10h6M9 14h4"/></svg><span class="n">3</span></div><h3>Finanzierung prüfen</h3><p>Wir finden die passende Lösung für<br>Ihr Unternehmen.</p></div>
      <div class="step"><div class="c"><svg class="ic" viewBox="0 0 24 24"><path d="M5 19l4-1-3-3zM14 4c3 0 6 3 6 6l-7 7-6-6z"/><circle cx="15" cy="9" r="1.5"/></svg><span class="n">4</span></div><h3>Umsetzung starten</h3><p>Schnell, zuverlässig und<br>partnerschaftlich.</p></div>
    </div>
  </div>
</section>

<section class="inquiry">
  <div class="wrap">
    <h2>Jetzt unverbindlich anfragen</h2>
    <p class="sub">Wir beraten Sie persönlich und finden die passende Lösung.</p>
    <div class="form">
      <div class="frow"><span class="field">Name</span><span class="field">Firma</span></div>
      <div class="frow"><span class="field">E-Mail</span><span class="field">Telefon</span></div>
      <span class="field full">Finanzierungsbedarf wählen <svg class="ic" viewBox="0 0 24 24"><path d="M6 9l6 6 6-6"/></svg></span>
      <span class="field area">Nachricht (optional)</span>
      <div class="consent"><i></i><span>Ich stimme der Verarbeitung meiner Daten gemäß <a>Datenschutzerklärung</a> zu.</span></div>
      <span class="btn btn-green submit">Anfrage absenden <svg class="ic" viewBox="0 0 24 24"><path d="M5 12h14M13 6l6 6-6 6"/></svg></span>
    </div>
    <div class="side" style="top:137px;height:221px">
      <span class="ico"><svg class="ic" viewBox="0 0 24 24"><path d="M5 4h4l2 5-2.5 1.5a11 11 0 005 5L15 13l5 2v4a2 2 0 01-2 2A16 16 0 013 6a2 2 0 012-2z"/></svg></span>
      <h3>Wir melden uns zeitnah persönlich zurück.</h3>
      <ul>
        <li><svg class="ic" viewBox="0 0 24 24"><circle cx="12" cy="12" r="9"/><path d="M8 12l3 3 5-6"/></svg>Persönliche Beratung</li>
        <li><svg class="ic" viewBox="0 0 24 24"><circle cx="12" cy="12" r="9"/><path d="M8 12l3 3 5-6"/></svg>Schnelle Rückmeldung</li>
        <li><svg class="ic" viewBox="0 0 24 24"><circle cx="12" cy="12" r="9"/><path d="M8 12l3 3 5-6"/></svg>Individuelle Lösung</li>
        <li><svg class="ic" viewBox="0 0 24 24"><circle cx="12" cy="12" r="9"/><path d="M8 12l3 3 5-6"/></svg>100% unverbindlich</li>
      </ul>
    </div>
    <div class="side" style="top:380px;height:148px">
      <span class="ico" style="background:#f1f3f7;color:#4b5563"><svg class="ic" viewBox="0 0 24 24"><rect x="3" y="5" width="18" height="16" rx="2"/><path d="M3 10h18M8 3v4M16 3v4"/></svg></span>
      <h3 style="font-size:14px">Alternativ: Termin vereinbaren</h3>
      <p>Buchen Sie direkt einen Termin in unserem Kalender.</p>
      <span class="link">Zum Terminkalender <svg class="ic" viewBox="0 0 24 24"><path d="M5 12h14M13 6l6 6-6 6"/></svg></span>
    </div>
  </div>
</section>

<section class="about">
  <div class="wrap">
    <span class="eyebrow">Über velacap</span>
    <h2>Kapital. Einfach. Jetzt.</h2>
    <div class="txt">
      <p>velacap steht für einfache, klare und schnelle Kapital- und Finanzierungslösungen für Unternehmen.</p>
      <p>Unser Fokus liegt auf Rechenzentren, digitaler Infrastruktur und nachhaltigem Wachstum. Wir verstehen die speziellen Anforderungen dieser Branchen und bieten maßgeschneiderte Lösungen.</p>
    </div>
    <div class="vals">
      <div class="val"><svg class="ic" viewBox="0 0 24 24"><rect x="5" y="3" width="14" height="18" rx="1.5"/><path d="M9 7h2M13 7h2M9 11h2M13 11h2M10 21v-4h4v4"/></svg><b>Erfahrung</b><p>Langjährige Expertise in Finanzierung und Kapitallösungen.</p></div>
      <div class="val"><svg class="ic" viewBox="0 0 24 24"><path d="M3 10l4-4 5 3 5-3 4 4-4 5-5 4-5-4z"/><path d="M9 12l3 2 3-2"/></svg><b>Partnerschaft</b><p>Wir denken mit und handeln in Ihrem Interesse.</p></div>
      <div class="val wide"><svg class="ic" viewBox="0 0 24 24"><circle cx="12" cy="12" r="9"/><path d="M8 12l3 3 5-6"/></svg><b>Verlässlichkeit</b><p>Klarheit, Transparenz und Verbindlichkeit im gesamten Prozess.</p></div>
    </div>
  </div>
</section>

<section class="ctawrap">
  <div class="wrap">
    <div class="ctabox">
      <h2>Bereit, Ihr Vorhaben zu finanzieren?</h2>
      <p>Stellen Sie jetzt Ihre Anfrage oder vereinbaren Sie direkt einen Termin mit einem unserer Experten.</p>
      <div class="acts">
        <span class="btn btn-green">Anfrage stellen <svg class="ic" viewBox="0 0 24 24"><path d="M5 12h14M13 6l6 6-6 6"/></svg></span>
        <span class="btn btn-ghost">Termin vereinbaren <svg class="ic" viewBox="0 0 24 24"><rect x="3" y="5" width="18" height="16" rx="2"/><path d="M3 10h18M8 3v4M16 3v4"/></svg></span>
      </div>
    </div>
  </div>
</section>

<footer class="footer">
  <div class="wrap">
    <div class="fcol" style="left:0">
      <div class="flogo"><i></i>velacap</div>
      <p class="addr"><b>Velacap GmbH</b><br>Kaimauer 7<br>22607 Hamburg</p>
    </div>
    <div class="fcol" style="left:266px">
      <h4>Kontakt</h4>
      <ul>
        <li><svg class="ic" viewBox="0 0 24 24"><path d="M5 4h4l2 5-2.5 1.5a11 11 0 005 5L15 13l5 2v4a2 2 0 01-2 2A16 16 0 013 6a2 2 0 012-2z"/></svg>+49 151 000 4821 37</li>
        <li><svg class="ic" viewBox="0 0 24 24"><rect x="3" y="5" width="18" height="14" rx="2"/><path d="M3 7l9 6 9-6"/></svg>info@velacap.de</li>
      </ul>
    </div>
    <div class="fcol" style="left:533px">
      <h4>Lösungen</h4>
      <ul><li>Rechenzentren</li><li>Gewerbefinanzierung</li><li>Baufinanzierung</li><li>Versicherungen</li><li>Kapitalanlage</li></ul>
    </div>
    <div class="fcol" style="left:800px">
      <h4>Rechtliches</h4>
      <ul><li>Datenschutz</li><li>Impressum</li><li>Cookie-Einstellungen</li></ul>
    </div>
    <div class="copy">© 2024 Velacap GmbH. Alle Rechte vorbehalten.</div>
  </div>
</footer>

</body>
</html>
```